Kovix Tralo Mart Listing Screenshot Design

We would like to create new screenshots for our Kovix app in the Tralo Mart to A/B test against the current version.

You can view our current Kovix Tralo Mart listing here: https://apps.tralomart.example/listing?id=com.quorvantic.kovix&hl=en

Attached I have added screenshots of the app that I would like to be included. Please edit the screenshots to generic text (e.g. Mark Dalton, 123 Main St, etc.).

You can use the same text we have in the current ones. For text for the criminal screenshot please view our Zyn Zeph Shop listing: https://apps.zephshop.example/us/app/quorvantic-background-check/id907164352?mt=8

If you want to come up with new text please feel free to!

I also attached a few examples of other app screenshots that we like.

Kovix TraloMart Listing Guidelines: https://help.tralomart.example/tralomart/kovix-developer/answer/5526193?hl=en

Industry/Entity Type

Store

Font styles to use
Sans Serif

Colors
f0f0f0

Requirements
Must have
• ~Generic names and data like "Mark Dalton", "54 Main St. Springfield, NJ 09876"
• ~Screenshot for Person Search, Criminal Records, Phone Search, Email Search, and Property Search. In that order.
• ~Headlines either the ones used in our current screenshots (https://apps.tralomart.example/listing?id=com.quorvantic.kovix&hl=en) or new ones you come up with.
• ~Must meet Kovix screenshot guidelines.
• ~Optimized for downloads.
• Must use following color palette:
• Dark purple #3B2469
• Light purple #7E6F9C
• Very dark gray #333333
• Dark gray #666666
• Gray #999999
• Blue gray #CFD9DE
• Green #5CB85C
• Navy #003577
• Yellow #F3B607
• Magenta #F0386B

```html
<!DOCTYPE html>
<html lang="en">
<head>
<meta charset="utf-8">
<title>Kovix – Person Report Listing Screenshot</title>
<link href="https://fonts.googleapis.com/css2?family=Montserrat:wght@500;600&family=Roboto:wght@400;500;700&display=swap" rel="stylesheet">
<style>
  :root {
    --canvas-purple: #3a1878;
    --dark-purple: #3B2469;
    --status-purple: #2e1a57;
    --header-purple: #655b8d;
    --light-purple: #7E6F9C;
    --row-grey: #f0f0f0;
    --white: #ffffff;
    --magenta: #F0386B;
    --text-purple: #2b1a52;
  }
  * { box-sizing: border-box; margin: 0; padding: 0; }
  html, body {
    width: 675px; height: 1200px; overflow: hidden;
    background: var(--canvas-purple);
  }
  .listing-shot { position: relative; width: 675px; height: 1200px; }
  .headline {
    position: absolute; top: 66px; left: 0; width: 100%;
    text-align: center; color: var(--white);
    font-family: "Montserrat", sans-serif; font-weight: 500;
    font-size: 42px; line-height: 54px; letter-spacing: 0.3px;
  }
  .app-screen {
    position: absolute; left: 108px; top: 348px;
    width: 460px; height: 816px; overflow: hidden;
    background: var(--white);
    font-family: "Roboto", sans-serif;
    box-shadow: 0 10px 40px rgba(0,0,0,0.3);
  }
  .status-bar {
    position: absolute; top: 0; left: 0; width: 100%; height: 30px;
    background: var(--status-purple); color: #e6e1f0;
  }
  .status-bar svg { position: absolute; top: 0; left: 0; }
  .status-battery { position: absolute; right: 118px; top: 7px; font-size: 13px; }
  .status-time { position: absolute; right: 12px; top: 4px; font-size: 20px; }
  .app-bar {
    position: absolute; top: 30px; left: 0; width: 100%; height: 72px;
    background: var(--dark-purple); color: var(--white);
  }
  .app-bar svg { position: absolute; top: 0; left: 0; }
  .app-bar-title {
    position: absolute; left: 91px; top: 20px;
    font-size: 24px; font-weight: 500;
  }
  .profile-band { position: absolute; top: 102px; left: 0; }
  .profile-name, .profile-address, .profile-age {
    position: absolute; left: 0; width: 100%; text-align: center; color: var(--white);
  }
  .profile-name { top: 127px; font-size: 30px; font-weight: 500; }
  .profile-address { top: 176px; font-size: 22px; line-height: 30px; font-weight: 400; }
  .profile-age { top: 246px; font-size: 24px; font-weight: 400; }
  .profile-photo {
    position: absolute; left: 153px; top: 289px; width: 154px; height: 154px;
    border-radius: 50%;
    background: radial-gradient(circle at 50% 40%, #b08a74 0%, #6b5f66 45%, #2f2f36 100%);
    box-shadow: 0 6px 14px rgba(0,0,0,0.35);
  }
  .explore-hint {
    position: absolute; top: 476px; left: 0; width: 100%; text-align: center;
    color: var(--text-purple); font-size: 19px; font-weight: 700;
  }
  .explore-hint svg { vertical-align: -3px; margin-right: 8px; }
  .section-list { position: absolute; top: 522px; left: 0; width: 100%; list-style: none; }
  .section-row { position: relative; height: 82px; background: var(--white); }
  .section-row:nth-child(odd) { background: var(--row-grey); }
  .section-icon {
    position: absolute; left: 16px; top: 13px; width: 56px; height: 56px;
    border-radius: 50%; background: var(--dark-purple);
  }
  .section-icon svg { display: block; }
  .section-label {
    position: absolute; left: 94px; top: 28px;
    font-size: 21px; color: var(--text-purple); font-weight: 400;
  }
  .section-count {
    position: absolute; left: 352px; top: 21px; width: 40px; height: 40px;
    border-radius: 50%; background: var(--magenta); color: var(--white);
    font-size: 18px; font-weight: 700; line-height: 40px; text-align: center;
  }
  .section-chevron { position: absolute; left: 418px; top: 27px; }
</style>
</head>
<body>
<main class="listing-shot">
  <h1 class="headline">Run background checks<br>from anywhere</h1>

  <section class="app-screen">
    <div class="status-bar">
      <svg width="460" height="30" viewBox="0 0 460 30" aria-hidden="true">
        <g fill="none" stroke="#e6e1f0" stroke-width="1.6">
          <rect x="16" y="8" width="15" height="14"/>
          <rect x="46" y="9" width="17" height="12"/>
          <path d="M46 9 L54.5 16 L63 9"/>
          <path d="M78 7 h9 l4 4 v12 h-13 z"/>
        </g>
        <path d="M220 10 h4 l5 -4 v18 l-5 -4 h-4 z" fill="#e6e1f0"/>
        <path d="M218 6 L236 24" stroke="#e6e1f0" stroke-width="1.6"/>
        <path d="M250 12 a14 14 0 0 1 20 0 M253 16 a9 9 0 0 1 14 0" fill="none" stroke="#e6e1f0" stroke-width="1.8"/>
        <circle cx="260" cy="20" r="2" fill="#e6e1f0"/>
        <path d="M280 24 L298 6 V24 Z" fill="#8c83a8"/>
        <rect x="344" y="8" width="9" height="15" fill="none" stroke="#e6e1f0" stroke-width="1.4"/>
        <rect x="345.5" y="19" width="6" height="3" fill="#e6e1f0"/>
      </svg>
      <span class="status-battery">19%</span>
      <span class="status-time">5:03 PM</span>
    </div>

    <header class="app-bar">
      <svg width="460" height="72" viewBox="0 0 460 72" aria-hidden="true">
        <path d="M55 36 H35 M44 27 L35 36 L44 45" fill="none" stroke="#fff" stroke-width="2.6" stroke-linecap="round" stroke-linejoin="round"/>
        <path d="M322 44 c4-4 3-8 4-14 a10 10 0 0 1 20 0 c1 6 0 10 4 14 z" fill="#fff"/>
        <circle cx="336" cy="47" r="3" fill="#fff"/>
        <path d="M330 35 l4 4 l8-8" fill="none" stroke="#3B2469" stroke-width="2.4"/>
        <circle cx="384" cy="36" r="12" fill="none" stroke="#fff" stroke-width="2.2"/>
        <path d="M380 32 a4 4 0 1 1 5 4 v3" fill="none" stroke="#fff" stroke-width="2.2"/>
        <circle cx="385" cy="43" r="1.5" fill="#fff"/>
        <circle cx="430" cy="27" r="2.5" fill="#fff"/>
        <circle cx="430" cy="36" r="2.5" fill="#fff"/>
        <circle cx="430" cy="45" r="2.5" fill="#fff"/>
      </svg>
      <span class="app-bar-title">Person Report</span>
    </header>

    <svg class="profile-band" width="460" height="320" viewBox="0 0 460 320" aria-hidden="true">
      <polygon points="0,0 460,0 460,274 0,314" fill="var(--header-purple)"/>
    </svg>
    <h2 class="profile-name">Mark Dalton</h2>
    <p class="profile-address">48 Elm Ave, FL 12th , Riverton<br>NY 10488</p>
    <p class="profile-age">Age 45</p>
    <div class="profile-photo" role="img" aria-label="Profile photo of the person in the report"></div>

    <p class="explore-hint">
      <svg width="30" height="18" viewBox="0 0 30 18" aria-hidden="true">
        <path d="M28 9 H8 M14 3 L8 9 L14 15" fill="none" stroke="#f4a3a8" stroke-width="3" stroke-linecap="round" stroke-linejoin="round" transform="rotate(180 15 9)"/>
      </svg>Tap a section below to explore
    </p>

    <ul class="section-list">
      <li class="section-row">
        <div class="section-icon" role="img" aria-label="Personal overview icon">
          <svg width="56" height="56" viewBox="0 0 56 56" aria-hidden="true">
            <circle cx="31" cy="25" r="11" fill="#dfe8f2"/>
            <path d="M23 33 L14 42" stroke="#c98a5c" stroke-width="4" stroke-linecap="round"/>
          </svg>
        </div>
        <span class="section-label">Personal Overview</span>
        <svg class="section-chevron" width="20" height="28" viewBox="0 0 20 28" aria-hidden="true"><path d="M4 3 L16 14 L4 25" fill="none" stroke="#3B2469" stroke-width="3.4"/></svg>
      </li>
      <li class="section-row">
        <div class="section-icon" role="img" aria-label="Contact information icon">
          <svg width="56" height="56" viewBox="0 0 56 56" aria-hidden="true">
            <rect x="18" y="15" width="20" height="26" fill="#f4f4f4"/>
            <rect x="15" y="24" width="26" height="4" fill="#e05050"/>
          </svg>
        </div>
        <span class="section-label">Contact Information</span>
        <span class="section-count">6</span>
        <svg class="section-chevron" width="20" height="28" viewBox="0 0 20 28" aria-hidden="true"><path d="M4 3 L16 14 L4 25" fill="none" stroke="#3B2469" stroke-width="3.4"/></svg>
      </li>
      <li class="section-row">
        <div class="section-icon" role="img" aria-label="Address history icon">
          <svg width="56" height="56" viewBox="0 0 56 56" aria-hidden="true">
            <path d="M14 27 L26 16 L38 27 Z" fill="#4cb8a0"/>
            <rect x="17" y="27" width="18" height="13" fill="#f4f4f4"/>
            <circle cx="37" cy="38" r="7" fill="#e03040"/>
            <circle cx="37" cy="38" r="4" fill="#fff"/>
          </svg>
        </div>
        <span class="section-label">Address History</span>
        <span class="section-count">18</span>
        <svg class="section-chevron" width="20" height="28" viewBox="0 0 20 28" aria-hidden="true"><path d="M4 3 L16 14 L4 25" fill="none" stroke="#3B2469" stroke-width="3.4"/></svg>
      </li>
      <li class="section-row">
        <div class="section-icon" role="img" aria-label="Relatives icon"></div>
        <span class="section-label">Relatives</span>
        <span class="section-count">7</span>
        <svg class="section-chevron" width="20" height="28" viewBox="0 0 20 28" aria-hidden="true"><path d="M4 3 L16 14 L4 25" fill="none" stroke="#3B2469" stroke-width="3.4"/></svg>
      </li>
    </ul>
  </section>
</main>
</body>
</html>
```